custom window treatments and soft furnishings

letterhead design/logo
a simple design that can be used on my invoices as well as as a logo
could be needle and thread, fabric rolls, window with draperies or a abstract design

Reason: I have been traveling and unable to view the designs.

Target Market(s)

women 35 and up who purchase custom made products

```html
<!DOCTYPE html>
<html lang="en">
<head>
<meta charset="utf-8">
<title>Fernhollow Studio — Letterhead</title>
<link rel="stylesheet" href="https://fonts.googleapis.com/css2?family=Almendra:wght@700&family=Roboto+Condensed:wght@700&display=swap">
<style>
  :root {
    --ink: #111111;
    --brand-blue: #2e78bb;
    --paper: #ffffff;
  }
  html, body {
    margin: 0;
    padding: 0;
    width: 900px;
    height: 1200px;
    overflow: hidden;
    background: var(--paper);
  }
  .letterhead {
    position: relative;
    width: 900px;
    height: 1200px;
    background: var(--paper);
  }
  .wordmark {
    position: absolute;
    left: 0;
    top: 0;
    width: 900px;
    height: 1200px;
  }
  .wordmark text {
    font-family: "Almendra", Georgia, serif;
    font-weight: 700;
    fill: var(--ink);
  }
  .rule {
    position: absolute;
    left: 125px;
    top: 665px;
    width: 628px;
    height: 16px;
    background: var(--brand-blue);
  }
  .contact {
    position: absolute;
    left: 125px;
    top: 688px;
    width: 631px;
    display: flex;
    justify-content: space-between;
    align-items: center;
    font-family: "Roboto Condensed", "Arial Narrow", sans-serif;
    font-weight: 700;
    font-size: 17px;
    line-height: 22px;
    color: var(--brand-blue);
    white-space: nowrap;
  }
  .contact .sep {
    width: 11px;
    height: 11px;
    background: var(--brand-blue);
    transform: rotate(45deg) scaleY(1.2);
  }
</style>
</head>
<body>
  <main class="letterhead">
    <svg class="wordmark" viewBox="0 0 900 1200" role="img" aria-label="Fernhollow Studio">
      <text x="124" y="587" font-size="82" textLength="615" lengthAdjust="spacingAndGlyphs">FERNHOLLOW</text>
      <text x="740" y="636" font-size="42" text-anchor="end" letter-spacing="6">STUDIO</text>
    </svg>

    <div class="rule"></div>

    <address class="contact">
      <span class="contact-address">42 Linden Row&nbsp;&nbsp;Marlow RI 02811</span>
      <span class="sep" aria-hidden="true"></span>
      <span class="contact-phone">401-555-0187</span>
      <span class="sep" aria-hidden="true"></span>
      <span class="contact-email">hello@fernhollowstudio.com</span>
    </address>
  </main>
</body>
</html>
```